Occupational Therapy Clinic Advertisement

Create an advertisement for a magazine. Below I have attached my original ad (Ad 2020.pdf) . I want the ad changed and it should be eye catching. I would like a eye catching graphics added in the ad. It should be a graphic image that applies to education. I am attaching a sample graphic image of that I liked from someone elses ad- it should not be the same- it just is there to show what I like. Please use the same words from my original ad.Dimensions: 3.75in x 10.3 in

Target Market(s)

Parents of School aged children

Requirements
Must have
• Must have eye catching Graphic. Colors should be eye catching for a typed magazine.

```html
<!DOCTYPE html>
<html lang="en">
<head>
<meta charset="utf-8">
<title>Bright Steps – OT Services</title>
<link rel="stylesheet" href="https://fonts.googleapis.com/css2?family=Montserrat:wght@400;500;600;700;800&display=swap">
<style>
  :root {
    --ink: #111418;
    --paper: #ffffff;
    --bubble-soft: #dcf0f2;
    --bubble-mid: #c4e6ea;
    --teal: #1ba9b2;
    --teal-ring: #bfe6e8;
    --pink: #e0245e;
    --pink-ring: #f6c3d3;
    --orange: #f6a53b;
    --orange-ring: #fbdcb2;
    --evaluate-red: #e8344e;
    --treat-orange: #f08a24;
    --bulb-yellow: #fcd54a;
  }
  * { margin: 0; padding: 0; box-sizing: border-box; }
  html, body { width: 1200px; height: 3298px; overflow: hidden; background: var(--paper); }
  body { font-family: "Montserrat", Arial, sans-serif; color: var(--ink); }
  .ad { position: relative; width: 1200px; height: 3298px; overflow: hidden; background: var(--paper); }
  .backdrop { position: absolute; inset: 0; }
  .abs { position: absolute; }

  .brand-name { top: 60px; left: 0; width: 100%; text-align: center; font-size: 90px; font-weight: 700; letter-spacing: 1px; }
  .service-info { top: 360px; left: 66px; }
  .service-title { font-size: 66px; font-weight: 500; line-height: 1.2; }
  .service-phone { font-size: 56px; font-weight: 500; margin-top: 14px; }
  .service-ages { font-size: 54px; font-weight: 700; margin-top: 24px; }
  .school-supplies-art { top: 200px; left: 545px; width: 620px; height: 540px; border-radius: 40px;
    background: linear-gradient(160deg, #cfeef1 0%, #f9d9a6 55%, #f3b8c8 100%); }

  .question-heading { top: 860px; left: 0; width: 100%; text-align: center; font-size: 70px; font-weight: 700; }
  .question { position: absolute; width: 290px; height: 290px; border-radius: 50%; display: flex; flex-direction: column;
    align-items: center; justify-content: center; text-align: center; color: #fff; padding: 0 42px; }
  .question::before { content: ""; position: absolute; inset: -22px; border-radius: 50%; z-index: -1; }
  .question-mark { font-size: 64px; font-weight: 800; line-height: 1; margin-bottom: 14px; }
  .question-text { font-size: 20px; font-weight: 700; text-transform: uppercase; line-height: 1.3; }
  .question--teal { left: 242px; top: 1002px; background: var(--teal); }
  .question--teal::before { background: var(--teal-ring); }
  .question--pink { left: 722px; top: 1055px; background: var(--pink); }
  .question--pink::before { background: var(--pink-ring); }
  .question--orange { left: 242px; top: 1313px; background: var(--orange); }
  .question--orange::before { background: var(--orange-ring); }
  .questions { position: absolute; inset: 0; z-index: 1; }

  .promise { top: 1670px; left: 0; width: 100%; text-align: center; font-size: 54px; font-weight: 600; line-height: 1.3; }
  .promise s { text-decoration-thickness: 4px; }

  .lightbulb-art { top: 1950px; left: 430px; width: 340px; height: 560px; border-radius: 170px 170px 60px 60px;
    background: radial-gradient(circle at 50% 35%, #fff1a8 0%, var(--bulb-yellow) 55%, #e9a92c 100%); }
  .we-badge { top: 2500px; left: 540px; width: 120px; height: 120px; border-radius: 50%; background: var(--treat-orange);
    border: 8px solid #fff; color: #fff; font-size: 40px; font-weight: 800; display: flex; align-items: center; justify-content: center; }

  .step { position: absolute; width: 380px; height: 290px; border-radius: 36px; color: #fff; padding: 110px 34px 0; }
  .step-number { position: absolute; top: -34px; width: 120px; height: 120px; border-radius: 50%; background: #fff;
    border: 12px solid currentColor; display: flex; align-items: center; justify-content: center; font-size: 44px; font-weight: 600; }
  .step-number span { color: var(--ink); }
  .step-title { font-size: 34px; font-weight: 800; text-transform: uppercase; }
  .step-text { font-size: 20px; font-weight: 700; text-transform: uppercase; line-height: 1.3; margin-top: 8px; }
  .step--evaluate { left: 20px; top: 2040px; background: var(--evaluate-red); color: #fff; }
  .step--evaluate .step-number { left: 30px; color: var(--evaluate-red); }
  .step--treat { left: 800px; top: 2060px; background: var(--treat-orange); }
  .step--treat .step-number { right: 30px; color: var(--treat-orange); }

  .footer { left: 0; width: 100%; text-align: center; font-weight: 600; text-transform: uppercase; font-size: 28px; line-height: 1.45; }
  .footer--rsa { top: 2790px; }
  .footer--location { top: 2970px; }
  .footer--contact { top: 3150px; }
</style>
</head>
<body>
<main class="ad">
  <svg class="backdrop" width="1200" height="3298" viewBox="0 0 1200 3298" aria-hidden="true">
    <circle cx="60" cy="40" r="300" fill="var(--bubble-soft)"/>
    <circle cx="1180" cy="60" r="220" fill="var(--bubble-soft)"/>
    <circle cx="20" cy="900" r="260" fill="var(--bubble-soft)"/>
    <circle cx="1150" cy="1320" r="360" fill="var(--bubble-soft)"/>
    <circle cx="560" cy="1250" r="170" fill="var(--bubble-mid)" opacity="0.5"/>
    <circle cx="120" cy="1950" r="240" fill="var(--bubble-soft)"/>
    <circle cx="1150" cy="2650" r="420" fill="var(--bubble-soft)"/>
    <circle cx="60" cy="3150" r="330" fill="var(--bubble-soft)"/>
    <circle cx="700" cy="3330" r="200" fill="var(--bubble-soft)"/>
  </svg>

  <h1 class="abs brand-name">Bright Steps</h1>

  <section class="abs service-info">
    <p class="service-title">OT Services</p>
    <p class="service-phone">(555) 014-2287</p>
    <p class="service-ages">Ages: 6-18</p>
  </section>
  <div class="abs school-supplies-art" role="img" aria-label="Illustration of stacked books, pencils in a cup and small children studying"></div>

  <h2 class="abs question-heading">Does your child</h2>
  <div class="questions">
    <div class="question question--teal"><span class="question-mark">!</span><span class="question-text">Struggle with reading/math?</span></div>
    <div class="question question--pink"><span class="question-mark">!</span><span class="question-text">Knows the information but fails the test?</span></div>
    <div class="question question--orange"><span class="question-mark">!</span><span class="question-text">Have difficulty remembering names and dates?</span></div>
  </div>

  <p class="abs promise">Yes Your Child <s>can</s> Will Succeed<br>in School!</p>

  <div class="abs lightbulb-art" role="img" aria-label="Illustration of a friendly light bulb character wearing glasses"></div>
  <div class="abs we-badge">WE</div>

  <div class="step step--evaluate">
    <div class="step-number"><span>01</span></div>
    <p class="step-title">Evaluate:</p>
    <p class="step-text">Using standardized evaluations</p>
  </div>
  <div class="step step--treat">
    <div class="step-number"><span>02</span></div>
    <p class="step-title">Treat:</p>
    <p class="step-text">Using researched based techniques, we treat the underlying processing</p>
  </div>

  <p class="abs footer footer--rsa">Board of Ed OT RSA's accepted</p>
  <p class="abs footer footer--location">Located in Borough Park<br>Evaluations done in Borough Park &amp; Staten Island<br>For more information or to be added to our email list,<br>please email: brightstepsot@example.com</p>
  <p class="abs footer footer--contact">Dana Lerner OTR/L<br>(555) 014-2287</p>
</main>
</body>
</html>
```